Bus Stop sign for cafe (retro caravan)

outdoor bus stop sign for EL PUMARÓN, produced in Aluminium Composite Panel (ACP).
Material & use
Material: ACP (outdoor suitable)
Installation: Outdoor bus stop (public area) – please recommend the best finish for weather + UV + potential vandalism exposure (e.g., anti-graffiti laminate).
Size (as measured)
My measurements are:
Side A: 2.60 m
Side B: 1.245 m
Side C: 1.725 m
Side D: 1.200 m
I would love a creative and efficient design, keep simple, effective but creative at the same time, maybe son retro vintage style.
The sign should include logo, photo of the caravan and basic information, that way clients can find El Pumarón.
the information is:
Coffee • Breakfast • Brunch
Open daily 7:00–12:30 | Closed Wednesdays
Keep the info block clean and minimal:
418 Wattlebrook Rd, Seabright Bay
@elpumaron_cafe
If you want to research more about my business visit my instagram @elpumaron_cafe or website www.elpumaron-kafe.com.au
Target Market(s)
tourist, locals,
Look and feel

```html
<!DOCTYPE html>
<html lang="en">
<head>
<meta charset="utf-8">
<title>El Pumarón – Bus Stop Sign</title>
<link href="https://fonts.googleapis.com/css2?family=Bebas+Neue&display=swap" rel="stylesheet">
<style>
  :root {
    --backdrop: #d1d3d4;
    --panel-white: #ffffff;
    --orange: #f28c4c;
    --orange-deep: #ec6f3f;
    --ink: #111111;
    --rule-grey: #8a8a8a;
  }
  * { margin: 0; padding: 0; box-sizing: border-box; }
  html, body {
    width: 882px; height: 1200px; overflow: hidden;
    background: var(--backdrop);
    font-family: "Bebas Neue", "Arial Narrow", sans-serif;
  }
  .sign {
    position: absolute; left: 129px; top: 81px;
    width: 596px; height: 1022px;
    background: var(--panel-white);
    clip-path: polygon(0 164px, 100% 0, 100% 100%, 0 100%);
  }
  .brand {
    position: absolute; left: 252px; top: 190px; width: 289px;
    text-align: center; color: var(--orange);
  }
  .brand-name { font-size: 70px; line-height: 1; letter-spacing: 1px; white-space: nowrap; }
  .brand-place { font-size: 22px; letter-spacing: 5px; margin-top: 6px; white-space: nowrap; }
  .accent-rule {
    position: absolute; left: 0; right: 0; top: 413px; height: 9px;
    background: var(--orange-deep);
  }
  .offer-band {
    position: absolute; left: 0; right: 0; top: 456px; height: 52px;
    background: var(--orange); color: var(--panel-white);
    font-size: 54px; line-height: 56px; text-align: center; white-space: nowrap;
  }
  .hours {
    position: absolute; left: 41px; top: 542px;
    color: var(--orange); font-size: 66px; line-height: 62px; white-space: nowrap;
  }
  .hours-divider {
    position: absolute; left: 284px; top: 537px; width: 2px; height: 144px;
    background: var(--rule-grey);
  }
  .closed-day {
    position: absolute; left: 311px; top: 548px;
    color: var(--ink); font-size: 60px; line-height: 60px; white-space: nowrap;
  }
  .info-panel {
    position: absolute; left: 0; right: 0; top: 704px; bottom: 0;
    background: linear-gradient(160deg, #f39455 0%, var(--orange) 50%, #ef8346 100%);
  }
  .pin-icon { position: absolute; left: 41px; top: 52px; width: 73px; height: 104px; }
  .address {
    position: absolute; left: 148px; top: 58px;
    color: var(--ink); font-size: 54px; line-height: 59px; white-space: nowrap;
  }
  .handle {
    position: absolute; left: 41px; top: 208px;
    color: var(--panel-white); font-size: 82px; line-height: 1; white-space: nowrap;
  }
</style>
</head>
<body>
  <div class="sign">
    <div class="brand">
      <div class="brand-name">El Pumarón</div>
      <div class="brand-place">Seabright Bay</div>
    </div>

    <div class="accent-rule"></div>
    <div class="offer-band">Coffee • Breakfast • Brunch</div>

    <div class="hours">Open Daily<br>7:00–12:30</div>
    <div class="hours-divider"></div>
    <div class="closed-day">Closed<br>Wednesdays</div>

    <div class="info-panel">
      <svg class="pin-icon" viewBox="0 0 84 112" aria-hidden="true">
        <path d="M42 4C22 4 8 18 8 37c0 22 34 55 34 55s34-33 34-55C76 18 62 4 42 4z" fill="#fff"/>
        <circle cx="42" cy="36" r="13" fill="var(--orange)"/>
        <path d="M20 88c-12 3-16 7-16 10 0 7 17 12 38 12s38-5 38-12c0-3-4-7-16-10" fill="none" stroke="#fff" stroke-width="8"/>
      </svg>
      <div class="address">418 Wattlebrook Rd,<br>Seabright Bay</div>
      <div class="handle">@elpumaron_cafe</div>
    </div>
  </div>
</body>
</html>
```